STAINLESS UNTESIL HOLDER AND UNTESIL SET DESIGN

I want two package design, one is for stainless utensil holder. another is for whole set of utensil with the stainless utensil holder.
The first product is just going to be the holder itself. The dimensions on this are. 4.3 x 4.3 x 7 in inches. That is what we would like the box to be

The second product is going to be the holder, but with the kitchen utensils as well. The dimensions are. 4.3 x 4.3 x 14.3 for the box as well.

For both products we would like a nice modern and sleek design showcasing our products. We would like our images to use, and not copies of similar products found online, this is important to us as there are slight differences with most found on the market. We will be attaching the pictures on a separate message.

Product 1 (holder alone) - We would like our logo (KW7) and product called Stainless Steel Holder. We would like to showcase some attributes written on the box, like a removable bottom easy for cleaning, lightweight, stainless steel.

Product 2- We would like our logo, and product to be called Kitchen Utensil Set with Holder. We would like a somewhat similar design to product 1 but with key features including the holder and also listed what is to be included in that set. Tongs, Ladle, turning spatula, spatula, spaghetti spoon, slotted spoon, holder.

we need to show: stainless utensil holder.
with a removable bottom
easy for cleaning, lightweight, stainless steel. (you can add some for us too if you have any idea better than us)
second product ,
we need to list 7 pcs kitchen utensil sets,
Tongs, Ladle, turning spatula, spatula, spaghetti spoon, slotted spoon, stainless holder.
silicone head, beech wood handle, NKR material ,(pls put on one NKR logo),BPA free, heat resistant up to 480 f, leaking removable bottom design for stainless holder, easy for cleaning, (if you have any suggestion, you can add for us)

Target Market(s)

Telvoro QPS, middle to higher class families, females 18-60

Other font styles liked:
• designer's choice

Requirements
Must have
• 2 designs one for just the holder the other for the utensils and holder
• sleek design
• Modern design
• Barcode
• Correct Dimensions
• PDF Source FIle
• Ready to print
• Our picture of our product,
Nice to have
• A great and very unique design that stands out
Should not have
• Other peoples product design copy and pasted
• Other peoples utensil set
• cheap crude design

```html
<!DOCTYPE html>
<html lang="en">
<head>
<meta charset="utf-8">
<title>KW7 Stainless Utensil Holder Package</title>
<link rel="stylesheet" href="https://fonts.googleapis.com/css2?family=Lato:wght@700;900&display=swap">
<style>
  :root {
    --pattern-brown: #3b3431;
    --pattern-brown-deep: #342e2b;
    --band-black: #000000;
    --title-white: #ffffff;
    --steel-light: #eef0f2;
    --steel-mid: #9aa0a6;
    --steel-dark: #4a4f55;
    --steel-blue: #2f6fb0;
    --brand-green: #6cb443;
    --brand-blue: #8fcdee;
  }
  * { margin: 0; padding: 0; box-sizing: border-box; }
  html, body { width: 737px; height: 1200px; overflow: hidden; background: #ffffff; }
  .package-face {
    position: relative;
    width: 737px;
    height: 1200px;
    font-family: "Lato", Arial, sans-serif;
  }
  .brand-panel {
    position: absolute;
    left: 0; top: 0;
    width: 737px; height: 394px;
    background: radial-gradient(ellipse at center, var(--pattern-brown) 0%, var(--pattern-brown-deep) 100%);
    display: flex;
    align-items: center;
    justify-content: center;
  }
  .brand-mark {
    display: flex;
    align-items: center;
    gap: 14px;
    margin-top: -10px;
  }
  .brand-dot {
    width: 26px; height: 26px;
    border-radius: 50%;
    background: var(--brand-blue);
  }
  .brand-name {
    font-weight: 900;
    font-size: 64px;
    letter-spacing: 2px;
    color: var(--brand-green);
    line-height: 1;
  }
  .title-band {
    position: absolute;
    left: 0; top: 394px;
    width: 737px; height: 292px;
    background: var(--band-black);
    text-align: center;
  }
  .title-material {
    position: absolute;
    left: 0; right: 0; top: 56px;
    font-weight: 900;
    font-size: 72px;
    line-height: 1;
    background: linear-gradient(180deg, var(--steel-light) 0%, var(--steel-mid) 45%, var(--steel-dark) 55%, var(--steel-light) 100%);
    -webkit-background-clip: text;
    background-clip: text;
    color: transparent;
  }
  .title-product {
    position: absolute;
    left: 0; right: 0; top: 148px;
    font-weight: 900;
    font-size: 68px;
    line-height: 1;
    color: var(--title-white);
    letter-spacing: 1px;
  }
  .product-photo {
    position: absolute;
    left: 0; top: 686px;
    width: 737px; height: 514px;
    background: linear-gradient(90deg,
      #8a8f94 0%, #e9ecef 12%, #f6f7f8 22%, #b9c0c6 32%,
      #5f6870 42%, #9aa4ad 52%, #2e6db1 62%, #7aa3cc 72%,
      #2a5f9c 84%, #6b7d90 100%);
  }
</style>
</head>
<body>
<main class="package-face">
  <section class="brand-panel" role="img" aria-label="Dark brown panel with a faint repeating pattern of pots, kettles and pans">
    <div class="brand-mark">
      <span class="brand-dot"></span>
      <span class="brand-name">KW7</span>
    </div>
  </section>
  <section class="title-band">
    <h2 class="title-material">Stainless</h2>
    <h1 class="title-product">UTENSIL HOLDER</h1>
  </section>
  <section class="product-photo" role="img" aria-label="Close-up photo of the polished stainless steel utensil holder with a round drain hole"></section>
</main>
</body>
</html>
```